Quotation and Scripture Design

We are a marketing firm looking for a graphic designer who is gifted in the merging of typestyles, colors, and composition into images suitable for framing in the home or office. The design criteria is quite simple, (1) keep it fresh without looking dated or religious, and (2) push the envelope a little with good, solid graphic design. Phase one will involve building our inventory of original artwork to fifty or more pieces to be marketed online. For phase two in addition to a line of greeting cards, we will also offer art pieces reproduced by laser engravers, CNC routers, chemical etching, and digital printers. For this reason it is necessary that all art files be submitted in a vector format.

Target Market(s)

Professional women and men who appreciate and purchase gallery quality artwork.

Industry/Entity Type

Graphic Designer

Requirements
Must have
• Selection of the designer will be based on their graphic interruption of the following two quotations.
Quotation No. 1 - Romans 8:28
And we know that all things work together for good to those who love God, to those who are called according to His purpose.
Quotation No. 2 -Jeremiah 29:11
For I know the plans I have for you, declares the Lord. Plans to prosper you and not to harm you. Plans to give you hope and a future.
Design one of these two formats to fit a 8" x10" frame, and the other to fit a 12" x 12" frame.
Nice to have
• Rich colors, fresh typestyles . . . please no Times Roman. Bold, creative composition is what we are looking for.
Should not have
• Dated, religious artwork found in the local bible bookstore is a very good example of what we DO NOT want. If it is not something you would purchase for yourself or a friend, more than likely it won't meet our criteria.

```html
<!DOCTYPE html>
<html lang="en">
<head>
<meta charset="utf-8">
<title>Jeremiah 29:11 — Scripture Print</title>
<link rel="stylesheet" href="https://fonts.googleapis.com/css2?family=Boogaloo&family=Oswald:wght@700&display=swap">
<style>
  :root {
    --wood-green: #6d8b3d;
    --wood-green-light: #78963f;
    --wood-green-dark: #627f36;
    --reference-ink: #4d5140;
    --verse-white: #ffffff;
  }
  html, body {
    margin: 0;
    padding: 0;
    width: 1200px;
    height: 1200px;
    overflow: hidden;
  }
  .print {
    position: relative;
    width: 1200px;
    height: 1200px;
  }
  .print__art {
    display: block;
    width: 1200px;
    height: 1200px;
  }
  .reference {
    font-family: "Oswald", "Arial Narrow", sans-serif;
    font-weight: 700;
    font-size: 168px;
    fill: var(--reference-ink);
    opacity: 0.92;
  }
  .verse {
    font-family: "Boogaloo", "Arial Narrow", sans-serif;
    font-size: 118px;
    fill: var(--verse-white);
    text-anchor: end;
  }
</style>
</head>
<body>
<main class="print">
  <svg class="print__art" viewBox="0 0 1200 1200" xmlns="http://www.w3.org/2000/svg">
    <defs>
      <linearGradient id="plank-tone" x1="0" y1="0" x2="1" y2="1">
        <stop offset="0" stop-color="var(--wood-green-dark)"/>
        <stop offset="0.5" stop-color="var(--wood-green)"/>
        <stop offset="1" stop-color="var(--wood-green-light)"/>
      </linearGradient>
    </defs>

    <rect class="backdrop" role="img" aria-label="Photo of green painted vertical wooden planks" x="0" y="0" width="1200" height="1200" fill="url(#plank-tone)"/>

    <text class="reference" transform="translate(30 28) rotate(90)" textLength="1137" lengthAdjust="spacingAndGlyphs">JEREMIAH 29:11</text>

    <g class="verse">
      <text x="1140" y="294" textLength="768" lengthAdjust="spacingAndGlyphs">For I know the plans</text>
      <text x="1137" y="416" textLength="543" lengthAdjust="spacingAndGlyphs">I have for you,</text>
      <text x="1135" y="538" textLength="677" lengthAdjust="spacingAndGlyphs">declares the Lord.</text>
      <text x="1158" y="660" textLength="781" lengthAdjust="spacingAndGlyphs">Plans to prosper you</text>
      <text x="1137" y="782" textLength="783" lengthAdjust="spacingAndGlyphs">and not to harm you.</text>
      <text x="1135" y="904" textLength="860" lengthAdjust="spacingAndGlyphs">Plans to give you hope</text>
      <text x="1155" y="1026" textLength="475" lengthAdjust="spacingAndGlyphs">and a future.</text>
    </g>
  </svg>
</main>
</body>
</html>
```